Business Card Design Project

We are an agricultural business based in Brisbane.
We design, manage and operate regional saleyards. Our logo is green/silver in colour and details of our business can be found on our website www.tovrak.com.au

Just wanting a corporate design for some business cards and include name, position, contact details.

Thanks

```html
<!DOCTYPE html>
<html lang="en">
<head>
<meta charset="utf-8">
<title>Tovrak Saleyards – Business Card</title>
<link href="https://fonts.googleapis.com/css2?family=Arimo:wght@400;700&family=PT+Serif:ital@1&display=swap" rel="stylesheet">
<style>
  :root {
    --page: #ffffff;
    --card: #ffffff;
    --steel: #7f7f7f;
    --steel-dark: #717171;
    --leaf: #00914b;
    --forest: #00723d;
    --ink: #222220;
    --text-grey: #666666;
    --edge: #1a1a1a;
  }
  * { margin: 0; padding: 0; box-sizing: border-box; }
  html, body {
    width: 1200px; height: 1000px; overflow: hidden;
    background: var(--page);
  }
  .card {
    position: absolute; left: 230px; top: 285px;
    width: 723px; height: 437px;
    background: var(--card);
    border-left: 1px solid var(--edge);
    border-right: 1px solid var(--edge);
    overflow: hidden;
  }
  .card__top-band {
    position: absolute; left: -1px; top: 0; width: 725px; height: 14px;
    background: var(--steel);
  }
  .tab { position: absolute; width: 16px; height: 54px; }
  .tab--grey { background: var(--steel-dark); top: 96px; }
  .tab--green { background: var(--leaf); top: 171px; }
  .tab--left { left: -1px; }
  .tab--right { right: -1px; }
  .card__base { position: absolute; left: -1px; top: 0; width: 725px; height: 437px; }
  .contact {
    position: absolute; left: 42px; top: 92px;
    font-family: "Arimo", Arial, sans-serif; color: var(--text-grey);
  }
  .contact__name {
    font-family: "PT Serif", Georgia, serif; font-style: italic; font-weight: 400;
    color: var(--forest); font-size: 31px; line-height: 40px; letter-spacing: 0.3px;
  }
  .contact__role { font-size: 20px; line-height: 24px; margin-top: -2px; }
  .contact__details { margin-top: 20px; font-size: 21px; line-height: 25px; }
  .brand {
    position: absolute; left: 368px; top: 300px; width: 330px;
    text-align: center;
    font-family: "Arimo", Arial, sans-serif; font-weight: 700;
    color: var(--ink); font-size: 33px; line-height: 36px; letter-spacing: 0.5px;
  }
</style>
</head>
<body>
  <div class="card">
    <div class="card__top-band"></div>
    <div class="tab tab--grey tab--left"></div>
    <div class="tab tab--green tab--left"></div>
    <div class="tab tab--grey tab--right"></div>
    <div class="tab tab--green tab--right"></div>

    <svg class="card__base" viewBox="0 0 725 437" aria-hidden="true">
      <polygon points="0,331 534,407 725,380 725,437 0,437" fill="var(--forest)"/>
    </svg>

    <div class="contact">
      <h1 class="contact__name">Daniel Hartwell</h1>
      <p class="contact__role">General Manager</p>
      <p class="contact__details">daniel@tovrak.com.au<br>Mob: 0412 555 019</p>
    </div>

    <div class="brand">TOVRAK<br>SALEYARDS</div>
  </div>
</body>
</html>
```